Apartment Investor Business Card Design

Need a new business card designed for my multifamily investment company

Industry/Entity Type

Real Estate

Contact Information for Business Card

Garrick Pelham - President & CEO
Brightwold Holdings, LLC
4838 North 92nd Avenue, Ste 500
Omaha, NE 68999
(402) 555-0147
Garrick@brightwoldholdings.example
Www.BrightwoldHoldings.example

Colors
3176b5

```html
<!DOCTYPE html>
<html lang="en">
<head>
<meta charset="utf-8">
<title>Brightwold Holdings — Business Card</title>
<link rel="stylesheet" href="https://fonts.googleapis.com/css2?family=Cinzel:wght@400;500&family=Lato:ital,wght@0,400;0,700;1,400&display=swap">
<style>
  :root {
    --brand-blue: #4a82c6;
    --brand-blue-deep: #3176b5;
    --card-paper: #efefef;
    --ink: #2b2b2b;
    --ink-soft: #5a5a5a;
    --rule: #c9c9c9;
    --backdrop: #3a3b3d;
    --white: #ffffff;
  }
  * { box-sizing: border-box; margin: 0; padding: 0; }
  html, body { width: 1200px; height: 896px; overflow: hidden; }
  body {
    background: var(--backdrop);
    display: flex;
    flex-direction: column;
    align-items: center;
    justify-content: center;
    gap: 40px;
    font-family: "Lato", sans-serif;
  }
  .card {
    width: 700px;
    height: 400px;
    position: relative;
    overflow: hidden;
  }

  /* Front */
  .card-front {
    background: var(--card-paper);
    border-bottom: 14px solid var(--brand-blue);
  }
  .holder {
    position: absolute;
    left: 56px;
    top: 58px;
  }
  .holder-name {
    font-family: "Cinzel", serif;
    font-weight: 400;
    font-size: 30px;
    letter-spacing: 1.5px;
    color: var(--brand-blue);
    line-height: 1;
  }
  .holder-title {
    font-size: 19px;
    color: var(--ink-soft);
    margin-top: 6px;
  }
  .contact-list {
    list-style: none;
    margin-top: 22px;
  }
  .contact-item {
    display: flex;
    align-items: center;
    gap: 10px;
    font-size: 16px;
    color: var(--ink);
    line-height: 1.45;
  }
  .contact-icon { width: 14px; height: 14px; flex: none; }

  .brand-lockup {
    position: absolute;
    right: 48px;
    top: 132px;
    display: flex;
    align-items: center;
    gap: 12px;
  }
  .brand-mark {
    width: 16px; height: 16px;
    background: var(--brand-blue);
    flex: none;
  }
  .brand-name {
    font-family: "Cinzel", serif;
    font-weight: 400;
    font-size: 26px;
    line-height: 1.15;
    letter-spacing: 2px;
    color: var(--ink-soft);
  }
  .brand-name span { display: block; }
  .divider {
    position: absolute;
    left: 300px;
    right: 40px;
    top: 238px;
    height: 1px;
    background: var(--rule);
  }
  .office {
    position: absolute;
    right: 52px;
    top: 256px;
    width: 330px;
    font-style: normal;
  }
  .office-company {
    font-size: 21px;
    color: var(--brand-blue);
    font-weight: 700;
  }
  .office-line {
    font-size: 19px;
    color: var(--ink);
    line-height: 1.3;
  }

  /* Back */
  .card-back {
    background: var(--brand-blue);
    display: flex;
    flex-direction: column;
    align-items: center;
    justify-content: center;
    gap: 28px;
  }
  .back-lockup {
    display: flex;
    align-items: center;
    gap: 16px;
  }
  .back-mark {
    width: 22px; height: 22px;
    border-radius: 50%;
    background: var(--white);
  }
  .back-name {
    font-family: "Cinzel", serif;
    font-weight: 400;
    font-size: 40px;
    letter-spacing: 3px;
    color: var(--white);
  }
  .back-web {
    font-size: 18px;
    color: var(--white);
    letter-spacing: 0.5px;
  }
</style>
</head>
<body>

<article class="card card-front">
  <div class="holder">
    <h1 class="holder-name">GARRICK PELHAM</h1>
    <p class="holder-title">President &amp; CEO</p>
    <ul class="contact-list">
      <li class="contact-item">
        <svg class="contact-icon" viewBox="0 0 16 16" aria-hidden="true"><path fill="#4a82c6" d="M2 5c0-2 2-3 6-3s6 1 6 3v1h-3V5H5v1H2zM3 7h10l1 7H2zM8 9a2 2 0 1 0 0 4 2 2 0 0 0 0-4z"/></svg>
        (402) 555-0147
      </li>
      <li class="contact-item">
        <svg class="contact-icon" viewBox="0 0 16 16" aria-hidden="true"><rect x="1" y="3" width="14" height="10" fill="#4a82c6"/><path d="M1 3l7 6 7-6" fill="none" stroke="#efefef" stroke-width="1.3"/></svg>
        Garrick@brightwoldholdings.example
      </li>
      <li class="contact-item">
        <svg class="contact-icon" viewBox="0 0 16 16" aria-hidden="true"><circle cx="8" cy="8" r="7" fill="#4a82c6"/><path d="M1 8h14M8 1c-3 3-3 11 0 14M8 1c3 3 3 11 0 14" fill="none" stroke="#efefef" stroke-width="1"/></svg>
        www.BrightwoldHoldings.example
      </li>
    </ul>
  </div>

  <div class="brand-lockup">
    <span class="brand-mark"></span>
    <span class="brand-name"><span>BRIGHTWOLD</span><span>HOLDINGS</span></span>
  </div>

  <div class="divider"></div>

  <address class="office">
    <p class="office-company">Brightwold Holdings, LLC</p>
    <p class="office-line">4838 North 92nd Avenue</p>
    <p class="office-line">Ste 500 Omaha, NE 68999</p>
  </address>
</article>

<article class="card card-back">
  <div class="back-lockup">
    <span class="back-mark"></span>
    <span class="back-name">BRIGHTWOLD HOLDINGS</span>
  </div>
  <p class="back-web">www.BrightwoldHoldings.example</p>
</article>

</body>
</html>
```